Training Course Info Brochure

Hi there, I'm looking for a design for A4 Flyer (2-3 pages) on our new Course - Infection Control. I have included a previous brochure on our courses so the designed can see the look and feel we are looking for.

As this is about Infection Control, I would also like to see some RED in the design or wording.

The brochure will need to include quite a few industry/ government logos as well and graphics are important. I have included some (Health Care Industry workers) and am also open to other graphics.

Thanks for considering!

Target Market(s)

The Health profession and students wanting to work in the health field

Industry/Entity Type

Health Care

Font styles to use
Sans Serif

Colors
3277b5
f78f20
ffffff
ec1f27

Requirements
Must have
• Similar feel to the brochure I have included in this brief.

SOME RED lettering as we are teaching Infection Control during the COVID19 pandemic
Nice to have
• Lovely design with quite a few photos graphics

Company details:

Carrow Academy of Learning
RTO 73648
FREECALL : 1800 437 982
www.carrowlearning.edu.au
info@carrowlearning.edu.au

```html
<!DOCTYPE html>
<html lang="en">
<head>
<meta charset="utf-8">
<title>Infection Control Skill Set – Carrow Academy of Learning</title>
<link href="https://fonts.googleapis.com/css2?family=Didact+Gothic&family=Nunito+Sans:wght@400;700;800&display=swap" rel="stylesheet">
<style>
  :root {
    --blue: #3277b5;
    --orange: #f78f20;
    --red: #ec1f27;
    --white: #ffffff;
    --ink: #231f20;
    --navy: #1f2a3a;
  }
  * { margin: 0; padding: 0; box-sizing: border-box; }
  html, body { width: 848px; height: 1200px; overflow: hidden; background: var(--white); }
  body { font-family: "Nunito Sans", Arial, sans-serif; color: var(--ink); }
  .page { position: relative; width: 848px; height: 1200px; overflow: hidden; }

  .heading { font-family: "Didact Gothic", "Century Gothic", sans-serif; font-weight: 400; letter-spacing: 0.5px; }
  .rule { display: block; width: 25px; height: 3px; margin-top: 6px; }

  .brand { position: absolute; left: 54px; top: 62px; width: 110px; display: flex; flex-direction: column; align-items: center; gap: 8px; }
  .brand-mark { width: 26px; height: 26px; background: var(--blue); }
  .brand-name { font-family: "Didact Gothic", sans-serif; font-size: 13px; line-height: 16px; text-align: center; color: var(--navy); }

  .cost { position: absolute; left: 433px; top: 46px; width: 380px; }
  .cost h2 { font-size: 19px; color: var(--orange); }
  .cost .rule { background: var(--orange); }
  .cost p { margin-top: 13px; font-size: 13px; line-height: 17px; }
  .cost .price { color: var(--red); }

  .hero { position: absolute; left: 0; top: 159px; width: 848px; height: 300px;
    background: radial-gradient(circle at 72% 42%, #8a6a6e 0 10%, #4a5566 26%, #2a3442 55%, #1c2330 100%); }
  .hero-art { position: absolute; inset: 0; background: radial-gradient(ellipse at 10% 85%, rgba(200,70,70,.55), transparent 45%), radial-gradient(circle at 64% 40%, rgba(205,80,75,.45), transparent 22%); }
  .hero-text { position: absolute; left: 51px; top: 42px; color: var(--white); }
  .hero-title { font-size: 41px; line-height: 44px; }
  .hero-sub { font-size: 26px; line-height: 30px; }
  .hero-line { width: 507px; height: 2px; background: var(--white); margin: 24px 0 20px; }
  .hero-unit { font-family: "Nunito Sans", sans-serif; font-size: 21px; line-height: 27px; }

  .about { position: absolute; left: 0; top: 486px; width: 415px; height: 502px; background: var(--blue);
    border-radius: 0 36px 36px 0; color: var(--white); padding: 20px 14px 0 51px; }
  .about h2 { font-size: 17px; }
  .about .rule { background: var(--white); margin-bottom: 9px; }
  .about p { font-size: 12.4px; line-height: 17px; margin-bottom: 9px; }
  .about strong { font-weight: 800; }

  .col { position: absolute; left: 446px; width: 362px; }
  .col h2 { font-size: 17.5px; line-height: 20px; }
  .col p { font-size: 12.4px; line-height: 17px; margin-bottom: 7px; }
  .col .lead { color: var(--red); margin-top: 14px; }
  .hl { color: var(--red); }
  .blue h2 { color: var(--blue); }
  .blue .rule { background: var(--blue); }
  .orange h2 { color: var(--orange); }
  .orange .rule { background: var(--orange); }
  .format { top: 496px; }
  .mentor { top: 842px; }
  .mentor p, .industry p { font-size: 12.4px; line-height: 18.5px; margin-top: 16px; }
  .industry { top: 1005px; }

  .partners { position: absolute; left: 96px; top: 1008px; width: 320px; }
  .partner { display: flex; align-items: center; gap: 12px; }
  .partner-mark { width: 40px; height: 40px; border-radius: 50%; background: #555; }
  .partner-name { font-size: 15px; font-weight: 700; color: var(--ink); }
  .partner-two { margin-top: 26px; }
  .partner-two .partner-name { color: var(--blue); font-size: 15px; }
  .partner-two .partner-mark { background: var(--blue); border-radius: 0; width: 22px; height: 22px; }

  .footer { position: absolute; left: 0; top: 1148px; width: 848px; height: 52px; display: flex; }
  .footer-contact { width: 593px; background: var(--orange); color: #fde3c6; padding-left: 51px; display: flex; align-items: center; font-size: 11.5px; letter-spacing: .3px; }
  .footer-web { flex: 1; background: var(--blue); color: #cfe0f0; display: flex; align-items: center; justify-content: flex-end; padding-right: 51px; font-size: 11.5px; letter-spacing: .3px; }
</style>
</head>
<body>
<div class="page">

  <div class="brand">
    <span class="brand-mark"></span>
    <span class="brand-name">Carrow Academy of Learning</span>
  </div>

  <section class="cost">
    <h2 class="heading">Course cost</h2>
    <span class="rule"></span>
    <p>Free infection control skill sets for everyone in Western Australia or <span class="price">$350/for students outside of WA.</span></p>
  </section>

  <header class="hero">
    <div class="hero-art" role="img" aria-label="Close-up illustration of red and grey coronavirus particles on a dark background"></div>
    <div class="hero-text">
      <h1 class="heading hero-title">Infection Control Skill set</h1>
      <p class="heading hero-sub">HLTSS00064 for Health Care workers</p>
      <div class="hero-line"></div>
      <p class="hero-unit">HLTINF001–Comply with infection prevention<br>and control policies and procedures</p>
    </div>
  </header>

  <section class="about">
    <h2 class="heading">About this course</h2>
    <span class="rule"></span>
    <p><strong>Protect yourself and others in the community from infectious diseases</strong></p>
    <p>There is not better time than now, to formally Upskill yourself and your team with a Nationally Accredited unit of Competency in Infection Control prevention <strong>including the latest COVID19 infection control protocols</strong> (Bureau of Community Health). Fast track your skills with Carrow’s Accredited Infection Control Skill set to get you job ready or enhance your current workplace skills.</p>
    <p>The COVID19 pandemic has highlighted the important of building the capacity and understanding of the workforce <strong>to practice safe infection control procedures.</strong></p>
    <p>This skill set will provide you with the skills and knowledge to assist in protecting yourself and others in the community from infectious diseases.</p>
    <p>You will understand how infections are spread, ways of preventing the spread of infection and how to protect yourself and others from infection.</p>
    <p>The skill set is becoming increasingly important for all Health Care Workers–and all workers are encouraged to upskill themselves today, whether you are becoming Job Ready or for your professional development in Industry.</p>
  </section>

  <section class="col blue format">
    <h2 class="heading">Course format–Online with face-to-face tutorial (in person or via LinkRoom)</h2>
    <span class="rule"></span>
    <p class="lead">Protect yourself and others in the community from infectious diseases</p>
    <p>Our course is delivered to you <span class="hl">online</span> which allows you to undertaken study at your own pace. It is recommended completion occurs within a month.</p>
    <p>You have completed the Online Component of your course, you are invited into a Practical Lab Session via face to face learning; to practice skills and undertake a workplace simulated activity.</p>
    <p>Regional locations may be fulfilled by LinkRoom technology and Carrow may also conduct on-site visits as required. Carrow also travel to regional locations throughout the year. Group training sessions are also available for corporates and workplaces.</p>
  </section>

  <section class="col orange mentor">
    <h2 class="heading">Mentor Support and Practical Sessions</h2>
    <span class="rule"></span>
    <p>Students are welcomed to the course by a short induction by your Tutor/Mentor to start you on your way with confidence! All of Carrow’s student resources, learner materials, videos are contained in Carrow’s easy to use LMS and learning is provided online at your convenience.</p>
  </section>

  <section class="col blue industry">
    <h2 class="heading">Industry Recognised</h2>
    <span class="rule"></span>
    <p>Carrow’s unique program in Infection Control is supported by leading Industry bodies, and includes certification by the Bureau of Community Health, and other leading Health bodies in Australia. Our Unit of competency is Australian Recognised and Accredited.</p>
  </section>

  <div class="partners">
    <div class="partner">
      <span class="partner-mark"></span>
      <span class="partner-name">Bureau of Community Health</span>
    </div>
    <div class="partner partner-two">
      <span class="partner-mark"></span>
      <span class="partner-name">National Council for Safe Patient Care</span>
    </div>
  </div>

  <footer class="footer">
    <div class="footer-contact">FREECALL : 1800 437 982 | info@carrowlearning.edu.au</div>
    <div class="footer-web">www.carrowlearning.edu.au</div>
  </footer>

</div>
</body>
</html>
```